Logo and label lay out for Copper Thistle wines

Wine Bottle label for single vineyard on The Mornington Peninsula, Victoria, Australia
Name of Vineyard is “Copper Thistle”
(A copper Thistle is a common biting ant found in the vineyard.)
The name and vintage of each of the four varieties of wine will need to be included on the label.
We want an instantly recognisable image on the label along with the name Copper Thistle.

Target Market(s)

Quality wine for cafes, restaurants and individual’s wine collection

Industry/Entity Type

Vineyard

Logo Text

Copper Thistle

Logo styles of interest
Emblem Logo
Abstract Logo
Colors

Designer to choose colors to be used in the design.

Requirements
Must have
• Simple yet stylish image, instantly recognisable .
Nice to have
• Possibly a stylistic image of an ant
Should not have
• Not an overly detailed image.

```html
<!DOCTYPE html>
<html lang="en">
<head>
<meta charset="utf-8">
<title>Copper Thistle – Chardonnay label</title>
<link rel="stylesheet" href="https://fonts.googleapis.com/css2?family=Jost:wght@400;500;600&display=swap">
<style>
  :root {
    --page: #ffffff;
    --paper: #f6f3ef;
    --ink: #0a0a0a;
    --reverse: #f6f3ef;
  }
  * { margin: 0; padding: 0; box-sizing: border-box; }
  html, body { width: 960px; height: 1200px; overflow: hidden; background: var(--page); }
  body { position: relative; font-family: "Jost", "Futura", sans-serif; color: var(--ink); }

  .dimension { position: absolute; }
  .dimension-width { left: 270px; top: 124px; width: 372px; height: 20px; }
  .dimension-height { left: 674px; top: 178px; width: 90px; height: 896px; }
  .dimension-label {
    position: absolute; font-size: 19px; font-weight: 400; letter-spacing: 5px; background: var(--page);
  }
  .dimension-width .dimension-label { left: 50%; top: -3px; transform: translateX(-50%); padding: 0 12px; }
  .dimension-height .dimension-label { left: 0; top: 432px; }

  .label {
    position: absolute; left: 268px; top: 178px; width: 377px; height: 897px;
    background: var(--paper); box-shadow: 0 1px 4px rgba(0,0,0,.25); overflow: hidden;
  }
  .ant-mark {
    position: absolute; left: 198px; top: 82px; width: 66px; height: 76px;
    background: radial-gradient(ellipse at center, #111 0 35%, rgba(17,17,17,.15) 70%, transparent 72%);
  }
  .band { position: absolute; left: 0; width: 100%; background: var(--ink); }
  .band-1 { top: 166px; height: 26px; }
  .band-2 { top: 216px; height: 29px; }
  .band-3 { top: 282px; height: 31px; }
  .band-4 { top: 357px; height: 32px; }
  .name-block { top: 416px; height: 248px; }

  .wine-name {
    position: absolute; left: 30px; top: 478px; color: var(--reverse);
    font-weight: 600; font-size: 38px; line-height: 76px; letter-spacing: 22px; text-transform: uppercase;
  }
  .variety {
    position: absolute; left: 30px; top: 722px;
    font-weight: 600; font-size: 25px; line-height: 29px; letter-spacing: 3.5px; text-transform: uppercase;
  }
  .origin {
    position: absolute; left: 32px; top: 808px;
    font-weight: 500; font-size: 18.5px; line-height: 25px; letter-spacing: 2.6px; text-transform: uppercase;
  }
</style>
</head>
<body>
  <div class="dimension dimension-width">
    <svg width="372" height="20" viewBox="0 0 372 20">
      <line x1="1" y1="4" x2="1" y2="16" stroke="#0a0a0a" stroke-width="2"/>
      <line x1="1" y1="10" x2="371" y2="10" stroke="#0a0a0a" stroke-width="2"/>
      <line x1="371" y1="4" x2="371" y2="16" stroke="#0a0a0a" stroke-width="2"/>
    </svg>
    <span class="dimension-label">40MM</span>
  </div>

  <div class="dimension dimension-height">
    <svg width="20" height="896" viewBox="0 0 20 896">
      <line x1="4" y1="1" x2="16" y2="1" stroke="#0a0a0a" stroke-width="2"/>
      <line x1="10" y1="1" x2="10" y2="400" stroke="#0a0a0a" stroke-width="2"/>
      <line x1="10" y1="494" x2="10" y2="895" stroke="#0a0a0a" stroke-width="2"/>
      <line x1="4" y1="895" x2="16" y2="895" stroke="#0a0a0a" stroke-width="2"/>
    </svg>
    <span class="dimension-label">95MM</span>
  </div>

  <section class="label">
    <div class="ant-mark" role="img" aria-label="Black ant silhouette standing on the top stripe"></div>
    <div class="band band-1"></div>
    <div class="band band-2"></div>
    <div class="band band-3"></div>
    <div class="band band-4"></div>
    <div class="band name-block"></div>
    <h1 class="wine-name">Copper<br>Thistle</h1>
    <p class="variety">Chardonnay<br>2018</p>
    <p class="origin">Single Vineyard<br>Mornington Peninsula</p>
  </section>
</body>
</html>
```